Business Card for a Floral & Decorating Business

I would like to take my current logo and create a better business card. I am looking for elegance as I am a florist and event decorator. My logo has multiple colour options. I like colours like green, purple, pink and orange, I think I would like a white card, open to black back ground. I want it to feel elegant and romantic. I like metallic lettering that maybe is indented in the paper, I also like glossy paper. I have a full logo already as well as a badge. I have attached both in multiple colours.m
Updates

Need extra days to review

Target Market(s)

Weddings, special events, floral customers

Industry/Entity Type

Floral and decorating

Contact Information for Business Card

Phone number, email, instagram, facebook, title, name, logo

Font styles to use
Script

Requirements
Nice to have
• Elegant

```html
<!DOCTYPE html>
<html lang="en">
<head>
<meta charset="utf-8">
<title>Maren Ellsworth – Business Card</title>
<link href="https://fonts.googleapis.com/css2?family=Allura&family=Poppins:wght@400;500&display=swap" rel="stylesheet">
<style>
  :root {
    --backdrop: #dedede;
    --card-white: #ffffff;
    --card-blush: #e8b8a8;
    --rose: #dca08f;
    --rose-light: #e6b9aa;
    --rose-faint: #f6e4dd;
    --blush-light: #f1cfc3;
    --brown: #5a2418;
    --ink: #1c1c1c;
    --shadow: #b5b5b5;
  }
  * { margin: 0; padding: 0; box-sizing: border-box; }
  html, body { width: 750px; height: 1200px; overflow: hidden; }
  body { background: var(--backdrop); position: relative; font-family: "Poppins", sans-serif; }

  .card {
    position: absolute; left: 65px; width: 620px; height: 355px; overflow: hidden;
    box-shadow: 6px 6px 0 var(--shadow);
  }
  .card--front { top: 205px; background: var(--card-white); }
  .card--back { top: 640px; background: var(--card-blush); }

  .floral { position: absolute; }
  .card--front .floral--top-right {
    left: 510px; top: 0; width: 110px; height: 90px;
    background: radial-gradient(ellipse at 70% 30%, var(--rose-faint), rgba(255,255,255,0) 72%);
  }
  .card--front .floral--bottom-left {
    left: 0; top: 240px; width: 123px; height: 115px;
    background: radial-gradient(ellipse at 35% 65%, var(--rose-faint), rgba(255,255,255,0) 72%);
  }
  .card--back .floral--top-right {
    left: 446px; top: 0; width: 174px; height: 272px;
    background: radial-gradient(ellipse at 65% 30%, var(--blush-light), rgba(232,184,168,0) 72%);
  }
  .card--back .floral--bottom-left {
    left: 0; top: 181px; width: 168px; height: 174px;
    background: radial-gradient(ellipse at 35% 65%, var(--blush-light), rgba(232,184,168,0) 72%);
  }

  .brand-mark {
    position: absolute; border-radius: 50%;
    display: flex; align-items: center; justify-content: center;
  }
  .brand-mark__name { font-family: "Poppins", sans-serif; font-weight: 400; font-size: 15px; white-space: nowrap; }
  .card--front .brand-mark {
    left: 63px; top: 95px; width: 168px; height: 168px; border: 1px solid var(--rose-light);
  }
  .card--front .brand-mark__name { color: var(--rose-light); }
  .card--back .brand-mark {
    left: 218px; top: 88px; width: 184px; height: 184px; border: 1px solid var(--brown);
  }
  .card--back .brand-mark__name { color: var(--brown); font-size: 16px; }

  .holder-name {
    position: absolute; left: 268px; top: 78px; max-width: 320px;
    font-family: "Allura", cursive; font-weight: 400; font-size: 46px; line-height: 1; white-space: nowrap;
  }
  .holder-name__first { color: var(--rose); }
  .holder-name__last { color: var(--brown); }

  .contact-rail {
    position: absolute; left: 270px; top: 154px; width: 30px; height: 112px;
    background: var(--rose); border-radius: 15px;
    display: flex; flex-direction: column; justify-content: space-around; align-items: center;
    padding: 6px 0;
  }
  .contact-rail svg { width: 14px; height: 14px; display: block; }

  .contact-list {
    position: absolute; left: 312px; top: 156px; list-style: none;
    color: var(--ink); font-size: 16.5px; font-weight: 400; line-height: 28px; white-space: nowrap;
  }
</style>
</head>
<body>

<section class="card card--front" aria-label="Business card front">
  <div class="floral floral--top-right" role="img" aria-label="Fine line-drawn tulips and blossoms in pale rose"></div>
  <div class="floral floral--bottom-left" role="img" aria-label="Fine line-drawn tulips and blossoms in pale rose"></div>

  <div class="brand-mark"><span class="brand-mark__name">Maren Ellsworth</span></div>

  <h1 class="holder-name"><span class="holder-name__first">Maren</span> <span class="holder-name__last">Ellsworth</span></h1>

  <div class="contact-rail" aria-hidden="true">
    <svg viewBox="0 0 16 16" fill="none" stroke="#fff" stroke-width="1.2" stroke-linecap="round" stroke-linejoin="round">
      <path d="M3 2.5l2.5-.5 1.3 3-1.5 1a8 8 0 0 0 4.2 4.2l1-1.5 3 1.3-.5 2.5C8 12.8 3.2 8 3 2.5z"/>
    </svg>
    <svg viewBox="0 0 16 16" fill="none" stroke="#fff" stroke-width="1.2" stroke-linejoin="round">
      <rect x="2" y="4" width="12" height="8.5"/><path d="M2 4l6 5 6-5M2 12.5l4.5-4M14 12.5l-4.5-4"/>
    </svg>
    <svg viewBox="0 0 16 16" fill="none" stroke="#fff" stroke-width="1.2">
      <circle cx="8" cy="8" r="5.5"/>
    </svg>
    <svg viewBox="0 0 16 16" fill="none" stroke="#fff" stroke-width="1.1">
      <circle cx="8" cy="8" r="6"/><ellipse cx="8" cy="8" rx="2.6" ry="6"/><path d="M2 8h12M3 5h10M3 11h10"/>
    </svg>
  </div>

  <ul class="contact-list">
    <li>555 0142 7788</li>
    <li>info@MarenEllsworth.com</li>
    <li>@MarenEllsworthDecor</li>
    <li>www.MarenEllsworth.com</li>
  </ul>
</section>

<section class="card card--back" aria-label="Business card back">
  <div class="floral floral--top-right" role="img" aria-label="White line-drawn tulips and falling petals"></div>
  <div class="floral floral--bottom-left" role="img" aria-label="White line-drawn tulips and blossoms"></div>

  <div class="brand-mark"><span class="brand-mark__name">Maren Ellsworth</span></div>
</section>

</body>
</html>
```